Velmora Skincare packaging designs

We are need to create packaging for our skincare brand. We need two designs. One for round jars which is for creams/capsules and the second will be for bottles/serums Some products will be larger in size so please ensure the packaging design will work and there isn't a lot white/empty space

Below are the names of some of our products.
Screw-On Top Jar (25 pads- 4 inches wide) - Glint Wipes I Skin Brightening Pads
Pump Bottle (2 oz) - ReVIVANT I Hyaluronic Acid + Vitamin Serum
Pump Bottle (6oz) - The Oat Rinse I Conditioning Face Cleanser
Dropper bottle (1 oz) - Quiet Glow I Hydrating Moisturizer
Cream jar (1.5 oz) - Quiet Glow I Hydrating Moisturizer
Capsules Jar (25 capsules in a jar)- Plume Drop I Moisture + Hydrating Capsules
Capsules Jar (25 capsules in a jar) - Clear Burst I Impurity Capsules

We will also need help with the packing design in terms of layout of the logo, item name, desc, and ingredients on each product.

Target Market(s)

women

Industry/Entity Type

skincare, beauty

Font styles to use
Sans Serif

Colors
E54698
E96AAD
F1A4CE
F9D9EA
FCEFF6

Requirements
Must have
• Pantone color is 2052 CP HEX #DAAFCA (218 , 175 , 202)

```html
<!DOCTYPE html>
<html lang="en">
<head>
<meta charset="utf-8">
<title>Velmora Skincare – Label Set</title>
<link rel="stylesheet" href="https://fonts.googleapis.com/css2?family=Montserrat:wght@400;500;700&family=Allura&display=swap">
<style>
  :root {
    --bg: #ffffff;
    --label: #f2f2f4;
    --label-edge: #e4e4e8;
    --lilac: #daafca;
    --lilac-soft: #c9a7cc;
    --ink: #1b1b1d;
    --ink-soft: #3a3a3e;
  }
  * { margin: 0; padding: 0; box-sizing: border-box; }
  html, body { width: 1200px; height: 1198px; overflow: hidden; background: var(--bg); }
  body { position: relative; font-family: "Montserrat", sans-serif; color: var(--ink); }

  .label {
    position: absolute;
    background: var(--label);
    border: 1px solid var(--label-edge);
    border-radius: 10px;
  }
  .label--serum   { left: 75px;  top: 400px; width: 245px; height: 710px; }
  .label--dropper { left: 397px; top: 620px; width: 258px; height: 470px; border-radius: 60px 60px 16px 16px; }
  .label--jar     { left: 717px; top: 832px; width: 435px; height: 260px; }

  .brand {
    position: absolute;
    font-weight: 500;
    color: var(--lilac-soft);
    letter-spacing: 0.12em;
    text-transform: uppercase;
    display: flex;
    align-items: center;
    gap: 8px;
  }
  .brand__dot { width: 9px; height: 9px; border-radius: 50%; background: var(--lilac); flex: none; }

  .product-vertical {
    position: absolute;
    font-weight: 700;
    color: var(--ink);
    transform: rotate(-90deg);
    transform-origin: left top;
    white-space: nowrap;
    letter-spacing: 0.01em;
  }
  .script { position: absolute; font-family: "Allura", cursive; color: var(--ink-soft); white-space: nowrap; }
  .desc { position: absolute; font-weight: 400; color: var(--ink-soft); white-space: nowrap; }
  .rule { position: absolute; height: 2px; background: var(--lilac); }
  .netwt { position: absolute; font-weight: 400; color: var(--ink-soft); white-space: nowrap; }

  /* serum */
  .label--serum .brand { left: 40px; top: 150px; font-size: 26px; }
  .label--serum .product-vertical { left: 160px; top: 490px; font-size: 30px; }
  .label--serum .script { left: 62px; top: 522px; font-size: 22px; }
  .label--serum .desc { left: 76px; top: 557px; font-size: 15px; }
  .label--serum .rule { left: 30px; top: 588px; width: 186px; }
  .label--serum .netwt { left: 50px; top: 603px; font-size: 12px; }

  /* dropper */
  .label--dropper .brand { left: 52px; top: 112px; font-size: 22px; }
  .label--dropper .product-vertical { left: 140px; top: 350px; font-size: 21px; }
  .label--dropper .script { left: 52px; top: 388px; font-size: 16px; }
  .label--dropper .rule { left: 52px; top: 412px; width: 138px; }
  .label--dropper .netwt { left: 65px; top: 422px; font-size: 10px; }

  /* jar */
  .label--jar .brand { left: 22px; top: 115px; font-size: 24px; }
  .label--jar .product-title { position: absolute; left: 186px; top: 68px; font-size: 33px; font-weight: 700; white-space: nowrap; }
  .label--jar .script { left: 210px; top: 120px; font-size: 19px; }
  .label--jar .rule { left: 205px; top: 166px; width: 204px; }
  .label--jar .netwt { left: 262px; top: 180px; font-size: 13px; }
</style>
</head>
<body>

  <section class="label label--serum" aria-label="ReVIVANT serum pump bottle label">
    <div class="brand"><span class="brand__dot"></span>Velmora</div>
    <div class="product-vertical">ReVIVANT</div>
    <div class="script">Hyaluronic Acid +</div>
    <div class="desc">Vitamin Serum</div>
    <div class="rule"></div>
    <div class="netwt">NET.WT 2 fl.oz 60 ml</div>
  </section>

  <section class="label label--dropper" aria-label="Quiet Glow dropper bottle label">
    <div class="brand"><span class="brand__dot"></span>Velmora</div>
    <div class="product-vertical">QUIET GLOW</div>
    <div class="script">Hydrating Moisturizer</div>
    <div class="rule"></div>
    <div class="netwt">NET.WT 1 fl.oz 30 ml</div>
  </section>

  <section class="label label--jar" aria-label="Quiet Glow cream jar label">
    <div class="brand"><span class="brand__dot"></span>Velmora</div>
    <div class="product-title">QUIET GLOW</div>
    <div class="script">Hydrating Moisturizer</div>
    <div class="rule"></div>
    <div class="netwt">NET.WT 1.5 fl.oz</div>
  </section>

</body>
</html>
```